Wine Radio Show web re-design

We need new website look for an unconventional, nationally-syndicated WINE RADIO show. Show is fun, hip, witty and covers all wine lifestyle topics. We are redesigning logo and looking for a redesign of our wordpress site that hosts all our audio podcasts, and the site design needs to leverage and maximize these podcasts. Do NOT use the logo currently on the website. The site is vinecorridor.com, please see more info on the attached.

Do NOT use the logo currently on the website. Please just typeset the name "Cellar Murmurs Radio".
Updates

Please do NOT use the logo from the current website. Please just use type (to match theme/deisgn) "Cellar Murmurs Radio". Thank you.

Hello Designers, Thank you for working on this project. A piece of feedback overall is that we'd like much less image/masthead space in general (the photos and images at the top). We'd like the navigation and the latest Cellar Murmurs podcast to be above the fold. Most of the wine imagery/scenery shots can be minimalized/drastically reduced/eliminated, to allow more room for the different sections. Hope that makes sense, and again, thank you for working on this!! Ruth

Target Market(s)

Wine lovers and wine industry professionals, probably 30+ years old

Industry/Entity Type

Radio

Font styles to use
Serif
Sans Serif
Decorative
Other font styles liked:
• Modern retro fonts

Requirements
Must have
• Must keep current content of site:
http://cellarmurmursradio.com/podcast/
Feature podcasts prominently.
Do NOT use the logo currently on the website.
Nice to have
• Graphics to consider incorporating:
• WINE: Grapes, wine glasses, wine bottles, wine pouring, corkscrews, grapevines, vineyards
• RADIO symbols: soundwaves, antenna, radio icon, Podcast symbols, microphone
Should not have
• Do NOT use current logo - just use type.

```html
<!DOCTYPE html>
<html lang="en">
<head>
<meta charset="utf-8">
<title>Cellar Murmurs Radio</title>
<link rel="stylesheet" href="https://fonts.googleapis.com/css2?family=Open+Sans:wght@400;600;700&family=Roboto+Slab:wght@400&display=swap">
<style>
:root{
  --wine:#9c1118;
  --wine-dark:#7a0b10;
  --orange:#e08a12;
  --orange-deep:#d87f0b;
  --title-orange:#e0861a;
  --rust:#c0560e;
  --ink:#222;
  --body:#666;
  --line:#dedede;
  --footer:#141414;
}
*{margin:0;padding:0;box-sizing:border-box}
html,body{width:692px;height:1200px;overflow:hidden;background:#fff}
body{position:relative;font-family:"Open Sans",Arial,sans-serif;color:var(--ink)}
.abs{position:absolute}

/* header */
.site-header{position:absolute;left:0;top:0;width:692px;height:60px;background:linear-gradient(#fff,#f6f6f6)}
.brand{position:absolute;left:69px;top:16px;font-family:"Roboto Slab",Georgia,serif;font-size:21px;color:var(--wine);white-space:nowrap}
.connect{position:absolute;left:561px;top:16px;font-size:8.5px;color:#666}
.social-top{position:absolute;left:563px;top:31px;display:flex;gap:5px}
.social-top span{width:15px;height:15px;border-radius:2px;display:block}

/* nav */
.main-nav{position:absolute;left:0;top:60px;width:692px;height:33px;background:linear-gradient(#b0141c,#8c0d13 60%,#76090e);display:flex;padding-left:69px}
.main-nav a{color:#fff;text-decoration:none;font-size:9.6px;line-height:33px;padding:0 8px;border-right:1px solid rgba(0,0,0,.35);box-shadow:1px 0 0 rgba(255,255,255,.12);white-space:nowrap}
.main-nav a:last-child{border-right:none;box-shadow:none}

/* compact hero */
.hero{position:absolute;left:0;top:93px;width:692px;height:160px;background:radial-gradient(circle at 75% 60%,#c9d24a 0%,#8faa2a 40%,#4f7a18 100%)}
.hero-visual{position:absolute;left:380px;top:0;width:312px;height:160px;background:linear-gradient(160deg,rgba(120,20,30,0) 20%,rgba(110,20,40,.55) 75%,rgba(90,50,30,.7))}
.hero h1{position:absolute;left:66px;top:32px;font-weight:400;font-size:21.5px;color:#fff;line-height:1.05}
.hero h1 span{display:block;font-size:18.5px;margin-top:3px}
.hero p{position:absolute;left:67px;top:83px;width:230px;font-size:7.6px;line-height:13px;color:#f3f3f3}
.dots{position:absolute;left:67px;top:119px;display:flex;gap:2px}
.dots i{width:7px;height:7px;border-radius:50%;background:#fff;display:block}

/* main */
.section-title{position:absolute;font-size:13.6px;font-weight:400;color:var(--ink);white-space:nowrap}
.photo{position:absolute}
.week-head{position:absolute;left:220px;top:298px;width:220px;font-size:8.6px;line-height:12px;color:#444}
.week-body{position:absolute;left:220px;top:328px;width:220px;font-size:6.5px;line-height:12px;color:var(--body)}
.rule{position:absolute;left:64px;width:376px;height:1px;background:var(--line)}
.ep-title{position:absolute;font-size:11.6px;color:var(--title-orange);white-space:nowrap}
.ep-text{position:absolute;width:180px;font-size:7.3px;line-height:11.5px;color:var(--body)}
.learn{position:absolute;font-size:7.3px;font-weight:700;color:#222;letter-spacing:.2px}
.post-title{position:absolute;font-size:9.2px;color:#333;white-space:nowrap}
.post-text{position:absolute;width:170px;font-size:7px;line-height:11.5px;color:var(--body)}
.post-meta{position:absolute;font-size:7px;color:var(--body);white-space:nowrap}
.btn-orange{position:absolute;width:61px;height:19px;background:linear-gradient(#ef9a25,#d4760a);color:#fff;font-size:7px;font-weight:600;text-align:center;line-height:19px;border-radius:2px}

/* sidebar */
.panel{position:absolute;left:458px;width:165px;border:1px solid #dcdcdc;border-radius:3px;background:#fff}
.panel-red-head{height:30px;background:linear-gradient(#b3151d,#8a0d13);border-radius:3px 3px 0 0;color:#fff;font-size:12px;padding:7px 14px}
.panel-grey-head{height:30px;background:linear-gradient(#fafafa,#ececec);border-bottom:1px solid #ddd;border-radius:3px 3px 0 0;color:#333;font-size:12px;padding:7px 14px}
.feat-title{position:absolute;left:14px;font-size:8.3px;color:#333}
.feat-text{position:absolute;left:14px;width:140px;font-size:6.5px;line-height:11px;color:var(--body)}
.btn-red{position:absolute;left:14px;width:68px;height:19px;background:linear-gradient(#c0171f,#950d13);color:#fff;font-size:7px;font-weight:600;text-align:center;line-height:19px;border-radius:2px}
.show-title{position:absolute;left:15px;font-size:8px;color:var(--title-orange)}
.show-text{position:absolute;left:15px;width:140px;font-size:6.4px;line-height:11px;color:var(--body)}
.newsletter{position:absolute;left:458px;top:734px;width:165px;height:90px;background:var(--orange-deep);color:#fff}
.newsletter h3{position:absolute;left:14px;top:12px;font-weight:400;font-size:13.4px;white-space:nowrap}
.newsletter p{position:absolute;left:15px;top:36px;font-size:6.4px}
.field{position:absolute;left:15px;top:48px;width:140px;height:18px;background:#fff;border-radius:2px;font-size:6.5px;color:#555;padding:4px 7px}
.field-btn{position:absolute;right:0;top:0;width:18px;height:18px;background:#5a2a0a;border-radius:0 2px 2px 0}
.player{position:absolute;left:454px;top:272px;width:169px;height:29px;border-radius:15px;background:linear-gradient(#eee,#bdbdbd);box-shadow:0 1px 2px rgba(0,0,0,.25)}
.player-track{position:absolute;left:30px;top:6px;width:110px;height:17px;border-radius:9px;background:linear-gradient(#9bcf2c,#5d9a10);font-size:4.8px;color:#fff;padding:5px 0 0 10px;white-space:nowrap}
.player-time{position:absolute;left:143px;width:20px;height:7px;border-radius:4px;font-size:4.5px;color:#fff;text-align:center;line-height:7px}

/* footer */
.site-footer{position:absolute;left:0;top:1024px;width:692px;height:176px;background:var(--footer)}
.foot-nav{position:absolute;left:66px;top:22px;font-size:8px;color:#fff;white-space:nowrap}
.foot-nav b{font-weight:400;margin:0 4px}
.copy{position:absolute;left:67px;top:41px;font-size:6.5px;color:#555}
.social-foot{position:absolute;left:558px;top:21px;display:flex;gap:2px}
.social-foot i{width:14px;height:14px;border-radius:50%;background:#fff;display:block}
</style>
</head>
<body>

<header class="site-header">
  <div class="brand">Cellar Murmurs Radio</div>
  <div class="connect">Get Connected</div>
  <div class="social-top" aria-label="Social links">
    <span style="background:#b52b27"></span><span style="background:#3b5b9a"></span><span style="background:#5bb9e6"></span>
  </div>
</header>

<nav class="main-nav">
  <a>HOME</a><a>EPISODE ARCHIVES</a><a>UNCORKED</a><a>ABOUT THE SHOW</a><a>ABOUT THE POST</a><a>ON THE AIR</a><a>BLOG</a><a>STORE</a>
</nav>

<section class="hero">
  <div class="hero-visual" role="img" aria-label="Glass of red wine, bottle and red grapes on a barrel in a sunny vineyard"></div>
  <h1>Mauris nunc quam venenatis<span>Aliquam volutpat Quisque</span></h1>
  <p>Etiam est nunc venenatis in tristique eu imperdiet ac nisl Cum sociis natoque penatibus et magnis dis parturient</p>
  <div class="dots"><i></i><i></i><i></i><i></i></div>
</section>

<main>
  <h2 class="section-title" style="left:64px;top:273px">This Week on Cellar Murmurs</h2>
  <div class="photo" style="left:66px;top:301px;width:144px;height:98px;background:linear-gradient(135deg,#2a0a0a,#5a0f14 50%,#1a0606)" role="img" aria-label="Wine bottle lying beside glasses and red grapes"></div>
  <div class="week-head">Mauris vel lacus vitae felis vestibulum volutpat Etiam est nunc venenatis in tristique</div>
  <div class="week-body">Phasellus felis dolor scelerisque a tempus eget lobortis id libero Donec scelerisque leo ac risus Praesent sit amet est In dictum dolor eu dictum porttitor enim felis viverra mi eget luctus massa purus quis odio Etiam nulla massa pharetra facilisis volutpat in imperdiet sit amet sem Aliquam nec erat at purus cursus interdum Vestibulum ligula augue bibendum accumsan vestibulum ut commodo a mi Morbi ornare</div>
  <div class="rule" style="top:425px"></div>

  <h2 class="section-title" style="left:62px;top:443px">Most Recent Episodes</h2>

  <div class="photo" style="left:62px;top:469px;width:176px;height:74px;background:linear-gradient(120deg,#f2b640,#d07a1c 45%,#4a3020)" role="img" aria-label="Grape clusters on the vine backlit by the sun"></div>
  <div class="ep-title" style="left:62px;top:547px">The Manipulation of Wine</div>
  <div class="ep-text" style="left:62px;top:565px">Mauris vel lacus vitae felis vestibulum volutpat Etiam est nunc venenatis in tristique eu</div>
  <div class="learn" style="left:62px;top:591px">LEARN MORE</div>

  <div class="photo" style="left:256px;top:468px;width:177px;height:74px;background:linear-gradient(120deg,#7a9a3a,#3e3a5a 50%,#8aa04a)" role="img" aria-label="Dark grape bunches hanging among green vine leaves"></div>
  <div class="ep-title" style="left:256px;top:545px">Three Wine festivals not to miss</div>
  <div class="ep-text" style="left:256px;top:563px">Mauris vel lacus vitae felis vestibulum volutpat Etiam est nunc venenatis in tristique eu</div>
  <div class="learn" style="left:256px;top:589px">LEARN MORE</div>

  <div class="photo" style="left:61px;top:617px;width:176px;height:73px;background:linear-gradient(#0a2a6a,#2a7ad8 50%,#0a2a6a)" role="img" aria-label="Glowing blue audio sound wave"></div>
  <div class="ep-title" style="left:60px;top:694px">Unusual Tastes</div>
  <div class="ep-text" style="left:60px;top:712px">Mauris vel lacus vitae felis vestibulum volutpat Etiam est nunc venenatis in tristique</div>
  <div class="learn" style="left:60px;top:738px">LEARN MORE</div>

  <div class="photo" style="left:255px;top:615px;width:177px;height:74px;background:linear-gradient(100deg,#2a1a14,#8a6a50 50%,#2a1a14)" role="img" aria-label="Row of wine bottles lying on a rack"></div>
  <div class="ep-title" style="left:255px;top:692px">A Rather Unhappy Customers</div>
  <div class="ep-text" style="left:255px;top:710px">Mauris vel lacus vitae felis vestibulum volutpat Etiam est nunc venenatis in tristique</div>
  <div class="learn" style="left:255px;top:736px">LEARN MORE</div>

  <div class="rule" style="top:771px"></div>

  <h2 class="section-title" style="left:63px;top:786px;color:var(--rust)">Most Recent Episodes</h2>

  <div class="post-title" style="left:64px;top:813px">Suspendisse quam leo molestie</div>
  <div class="post-text" style="left:64px;top:829px">Vivamus porttitor g purus nisi eleifend libero a tempus libero lectus feugiat felis Morb</div>
  <div class="post-meta" style="left:66px;top:858px">By Author Name &nbsp;|&nbsp; 03, June 2014</div>
  <div class="btn-orange" style="left:66px;top:873px">READ MORE</div>

  <div class="post-title" style="left:257px;top:813px">Phasellus pellentesque aliq</div>
  <div class="post-text" style="left:257px;top:829px">Vivamus porttitor g purus nisi eleifend libero a tempus libero lectus feugiat felis Morb</div>
  <div class="post-meta" style="left:258px;top:858px">By Author Name &nbsp;|&nbsp; 03, June 2014</div>
  <div class="btn-orange" style="left:258px;top:873px">READ MORE</div>

  <div class="post-title" style="left:65px;top:910px">Suspendisse quam molestie</div>
  <div class="post-text" style="left:65px;top:926px">Vivamus porttitor g purus nisi eleifend libero a tempus libero lectus feugiat felis Morb</div>
  <div class="post-meta" style="left:67px;top:955px">By Author Name &nbsp;|&nbsp; 03, June 2014</div>
  <div class="btn-orange" style="left:67px;top:970px">READ MORE</div>

  <div class="post-title" style="left:258px;top:910px">Aellentesque aliquam enim</div>
  <div class="post-text" style="left:258px;top:926px">Vivamus porttitor g purus nisi eleifend libero a tempus libero lectus feugiat felis Morb</div>
  <div class="post-meta" style="left:260px;top:955px">By Author Name &nbsp;|&nbsp; 03, June 2014</div>
  <div class="btn-orange" style="left:260px;top:970px">READ MORE</div>
</main>

<aside>
  <div class="player" aria-label="Audio player">
    <svg class="abs" style="left:4px;top:3px" width="23" height="23" viewBox="0 0 23 23"><circle cx="11.5" cy="11.5" r="10.5" fill="#d6d6d6" stroke="#9a9a9a"/><path d="M9 7l7 4.5-7 4.5z" fill="#6a9a1a"/></svg>
    <div class="player-track">Now playing: Episode 42</div>
    <svg class="abs" style="left:107px;top:4px" width="20" height="20" viewBox="0 0 20 20"><circle cx="10" cy="10" r="9" fill="#555" stroke="#ddd" stroke-width="1.5"/><circle cx="10" cy="10" r="3" fill="#999"/></svg>
    <div class="player-time" style="top:6px;background:#7ab020">02:58</div>
    <div class="player-time" style="top:16px;background:#888">2:54</div>
  </div>

  <div class="panel" style="top:312px;height:207px">
    <div class="panel-red-head">Featured Podcast</div>
    <div class="photo" style="left:14px;top:42px;width:139px;height:74px;background:linear-gradient(#e8b070,#7a8a4a 55%,#3a4a20)" role="img" aria-label="Wine barrels and a bottle in a vineyard at sunset"></div>
    <div class="feat-title" style="top:121px">Donec scelerisque leo risus</div>
    <div class="feat-text" style="top:133px">Praesent sit amet est In dictum dolor eu dictum porttitor enim felis viverra mi eget luctus massa purus quis odio</div>
    <div class="btn-red" style="top:171px">READ MORE</div>
  </div>

  <div class="panel" style="top:526px;height:199px">
    <div class="panel-grey-head">Recent Shows</div>
    <div class="show-title" style="top:41px">Episode Tittle Name</div>
    <div class="show-text" style="top:53px">Vestibulum ligula augue bibendum ac cumsan vestibulum comm</div>
    <div class="show-title" style="top:86px">Episode Tittle Name</div>
    <div class="show-text" style="top:98px">Malesuada nec ultricies sit amet porttitor mattis enim In massa libero interdum nec interdum vel blandit sed nulla</div>
    <div class="show-title" style="top:142px">Episode Tittle Name</div>
    <div class="show-text" style="top:154px">Vestibulum ligula augue bibendum accum-san vestibulum comm Vestibulum ligu</div>
  </div>

  <div class="newsletter">
    <h3>Newsletter Subscribe</h3>
    <p>Please sign up here for latest news.</p>
    <div class="field">email address<span class="field-btn"><svg width="18" height="18" viewBox="0 0 18 18"><path d="M7 5l5 4-5 4z" fill="#fff"/></svg></span></div>
  </div>
</aside>

<footer class="site-footer">
  <div class="foot-nav">HOME<b>|</b>EPISODE ARCHIVES<b>|</b>UNCORKED<b>|</b>ABOUT THE SHOW<b>|</b>ABOUT THE POST<b>|</b>ON THE AIR<b>|</b>BLOG<b>|</b>STORE</div>
  <div class="copy">© 2014 Company Name &nbsp;All right reserved &nbsp;Term of Use</div>
  <div class="social-foot" aria-label="Social links"><i></i><i></i><i></i><i></i></div>
</footer>

</body>
</html>
```